high end contractor

high end contracting company we do all phases of construction kitchen,bathrooms,etc... please look at my website before you design www.harborkeybuild.com

would love some sort of lines or logo or both

Industry/Entity Type

Construction

Contact Information for Business Card

company name: oak & meridian contracting address: 318 fenwick st mount Vernon ny 10552 email: harborkeybuild@mailbrook.com website: www.harborkeybuild.com office#: 914-208-3916 fax#: 914-208-5523 dominic valtersen mobile# 917-526-0389

```html
<!DOCTYPE html>
<html lang="en">
<head>
<meta charset="utf-8">
<title>Oak &amp; Meridian Contracting – Business Card</title>
<link href="https://fonts.googleapis.com/css2?family=Arimo:ital,wght@0,400;0,700;1,400;1,700&display=swap" rel="stylesheet">
<style>
  :root {
    --stage: #e9e7e4;
    --card: #ffffff;
    --card-shade: #f1f1f1;
    --brand-blue: #1c8fd0;
    --brand-green: #5f9a12;
    --ink: #2d2d2d;
    --muted: #444444;
  }
  * { box-sizing: border-box; margin: 0; padding: 0; }
  html, body { width: 1200px; height: 900px; overflow: hidden; }
  body {
    background: var(--stage);
    font-family: "Arimo", Arial, sans-serif;
    position: relative;
  }
  .card {
    position: absolute;
    width: 600px;
    height: 343px;
    border-radius: 22px;
    background: radial-gradient(ellipse at 60% 40%, var(--card) 0%, var(--card-shade) 100%);
    box-shadow: 0 10px 24px rgba(0,0,0,0.18);
    overflow: hidden;
  }
  .card--front { left: 60px; top: 60px; }
  .card--back { left: 540px; top: 490px; }

  .wordmark {
    display: flex;
    align-items: center;
    gap: 10px;
    color: var(--brand-green);
    font-weight: 700;
    font-size: 26px;
    line-height: 1.1;
  }
  .wordmark__mark {
    width: 16px; height: 16px;
    background: var(--brand-blue);
    flex: none;
  }
  .card--front .wordmark {
    position: absolute;
    left: 0; right: 0; top: 0; bottom: 0;
    justify-content: center;
  }

  .band { position: absolute; left: 0; top: 0; width: 140px; height: 343px; }

  .person { position: absolute; left: 150px; top: 72px; }
  .person__name {
    color: var(--brand-blue);
    font-weight: 700;
    font-style: italic;
    font-size: 28px;
  }
  .person__role {
    color: var(--ink);
    font-style: italic;
    font-size: 21px;
    margin-top: 8px;
  }
  .contacts {
    position: absolute;
    left: 150px; top: 200px;
    list-style: none;
    font-style: italic;
    font-size: 16px;
    color: var(--muted);
  }
  .contacts li {
    display: flex; align-items: center; gap: 10px;
    height: 25px;
  }
  .contacts svg { width: 15px; height: 15px; flex: none; }
  .card--back .wordmark {
    position: absolute;
    right: 36px; top: 150px;
    font-size: 21px;
    width: 220px;
  }
</style>
</head>
<body>
  <section class="card card--front" aria-label="Card front">
    <div class="wordmark">
      <span class="wordmark__mark"></span>
      <span>Oak &amp; Meridian Contracting</span>
    </div>
  </section>

  <section class="card card--back" aria-label="Card back">
    <svg class="band" viewBox="0 0 140 343" aria-hidden="true">
      <path d="M0 0 H102 C70 60 58 140 80 230 C92 280 100 315 104 343 H0 Z" fill="var(--brand-green)"/>
      <path d="M0 0 H86 C54 60 44 140 66 230 C78 280 86 315 90 343 H0 Z" fill="var(--brand-blue)"/>
    </svg>

    <div class="person">
      <h1 class="person__name">Dominic Valtersen</h1>
      <p class="person__role">Founder</p>
    </div>

    <ul class="contacts">
      <li>
        <svg viewBox="0 0 16 16" aria-hidden="true"><rect x="4" y="1" width="8" height="14" rx="1.5" fill="none" stroke="var(--brand-blue)" stroke-width="1.6"/><circle cx="8" cy="12.3" r="0.9" fill="var(--brand-blue)"/></svg>
        917-526-0389
      </li>
      <li>
        <svg viewBox="0 0 16 16" aria-hidden="true"><rect x="1" y="3" width="14" height="10" fill="var(--brand-blue)"/><path d="M1 3 L8 9 L15 3" fill="none" stroke="#fff" stroke-width="1.2"/></svg>
        harborkeybuild@mailbrook.com
      </li>
      <li>
        <svg viewBox="0 0 16 16" aria-hidden="true"><g fill="none" stroke="var(--brand-blue)" stroke-width="1.3"><circle cx="8" cy="8" r="6.5"/><ellipse cx="8" cy="8" rx="3" ry="6.5"/><path d="M1.5 8 H14.5 M3 4.5 H13 M3 11.5 H13"/></g></svg>
        www.harborkeybuild.com
      </li>
      <li>
        <svg viewBox="0 0 16 16" aria-hidden="true"><circle cx="8" cy="8" r="6.5" fill="var(--brand-blue)"/></svg>
        @oakmeridian
      </li>
    </ul>

    <div class="wordmark">
      <span class="wordmark__mark"></span>
      <span>Oak &amp; Meridian Contracting</span>
    </div>
  </section>
</body>
</html>
```